Brennick Capital Business Cards

These are professional business cards that are for my family office.
Put fake emails and phone numbers as of now until I finalize those components. This family office controls my families investments, assets, and future. The cards should be professional.
..
.
.
.
I just uploaded another variation of a logo I would like to see as a business card to I am inbeteen which logo to use

Target Market(s)

business

Industry/Entity Type

business

Contact Information for Business Card

Professional, wealth related, finance related.

Requirements
Must have
• Logo

```html
<!DOCTYPE html>
<html lang="en">
<head>
<meta charset="UTF-8">
<title>Brennick Capital Business Cards</title>
<link href="https://fonts.googleapis.com/css2?family=Playfair+Display:wght@400&family=Tinos:wght@400&display=swap" rel="stylesheet">
<style>
  :root {
    --backdrop: #2b2b2b;
    --card: #222222;
    --gold: #c5ad6b;
    --white: #ffffff;
    --ink: #1a1a1a;
    --edge: #d9d9d9;
  }
  * { box-sizing: border-box; margin: 0; padding: 0; }
  html, body { width: 1200px; height: 694px; overflow: hidden; }
  body {
    background: var(--backdrop);
    display: flex;
    align-items: center;
    justify-content: center;
    gap: 40px;
  }
  .card {
    position: relative;
    width: 540px;
    height: 309px;
    background: var(--card);
    box-shadow: 0 14px 40px rgba(0,0,0,0.45);
  }
  .card-frame {
    position: absolute;
    inset: 6px;
    border: 1px solid var(--edge);
    pointer-events: none;
  }
  .wordmark {
    display: flex;
    align-items: center;
    gap: 12px;
    font-family: "Playfair Display", serif;
    font-weight: 400;
    color: var(--white);
    letter-spacing: 0.08em;
    white-space: nowrap;
  }
  .wordmark-square {
    width: 14px;
    height: 14px;
    background: var(--gold);
    flex: none;
  }
  .card-front {
    display: flex;
    align-items: center;
    justify-content: center;
  }
  .card-front .wordmark { font-size: 38px; }

  .card-back .wordmark {
    position: absolute;
    top: 62px;
    left: 0;
    right: 0;
    justify-content: center;
    font-size: 30px;
  }
  .card-back .wordmark-square { width: 11px; height: 11px; }

  .holder {
    position: absolute;
    top: 160px;
    right: 290px;
    text-align: right;
    font-family: "Tinos", serif;
  }
  .holder-name { color: var(--gold); font-size: 22px; line-height: 1.1; }
  .holder-role { color: var(--white); font-size: 14px; margin-top: 3px; }

  .divider {
    position: absolute;
    left: 268px;
    top: 140px;
    width: 1px;
    height: 84px;
    background: linear-gradient(to bottom, rgba(197,173,107,0), var(--gold) 30%, var(--gold) 70%, rgba(197,173,107,0));
  }

  .contacts {
    position: absolute;
    left: 288px;
    top: 146px;
    list-style: none;
    font-family: "Tinos", serif;
    color: var(--white);
    font-size: 14px;
  }
  .contacts li {
    display: flex;
    align-items: center;
    gap: 10px;
    height: 24px;
  }
  .contacts svg { width: 14px; height: 14px; fill: var(--gold); flex: none; }

  .address-band {
    position: absolute;
    left: 6px;
    right: 6px;
    top: 246px;
    height: 28px;
    background: var(--gold);
    display: flex;
    align-items: center;
    justify-content: center;
    gap: 8px;
    font-family: "Tinos", serif;
    font-size: 14px;
    color: var(--ink);
  }
  .address-band svg { width: 12px; height: 15px; fill: var(--ink); }
</style>
</head>
<body>

  <section class="card card-front" aria-label="Card front">
    <div class="wordmark">
      <span class="wordmark-square"></span>
      <span>BRENNICK CAPITAL</span>
    </div>
  </section>

  <section class="card card-back" aria-label="Card back">
    <div class="wordmark">
      <span class="wordmark-square"></span>
      <span>BRENNICK CAPITAL</span>
    </div>

    <div class="holder">
      <p class="holder-name">Marcus Ellery</p>
      <p class="holder-role">Owner</p>
    </div>

    <span class="divider"></span>

    <ul class="contacts">
      <li>
        <svg viewBox="0 0 24 24" aria-hidden="true"><path d="M6.6 10.8a15.1 15.1 0 0 0 6.6 6.6l2.2-2.2a1 1 0 0 1 1-.25 11.4 11.4 0 0 0 3.6.57 1 1 0 0 1 1 1V20a1 1 0 0 1-1 1A17 17 0 0 1 3 4a1 1 0 0 1 1-1h3.5a1 1 0 0 1 1 1c0 1.25.2 2.45.57 3.57a1 1 0 0 1-.25 1z"/></svg>
        <span>044-123 456 789</span>
      </li>
      <li>
        <svg viewBox="0 0 24 24" aria-hidden="true"><path d="M2 5h20v14H2z" fill="none"/><path d="M2 5h20v2l-10 6L2 7z"/><path d="M2 9l10 6 10-6v10H2z"/></svg>
        <span>info@webname.com</span>
      </li>
      <li>
        <svg viewBox="0 0 24 24" aria-hidden="true"><path d="M12 2a10 10 0 1 0 0 20 10 10 0 0 0 0-20zm6.9 6h-2.9a15.7 15.7 0 0 0-1.4-3.6A8 8 0 0 1 18.9 8zM12 4c.8 1.2 1.5 2.5 1.9 4h-3.8c.4-1.5 1.1-2.8 1.9-4zM4.3 14a8 8 0 0 1 0-4h3.4a16.5 16.5 0 0 0 0 4zm.8 2h2.9c.3 1.3.8 2.5 1.4 3.6A8 8 0 0 1 5.1 16zM8 8H5.1a8 8 0 0 1 4.3-3.6C8.8 5.5 8.3 6.7 8 8zm4 12c-.8-1.2-1.5-2.5-1.9-4h3.8c-.4 1.5-1.1 2.8-1.9 4zm2.3-6H9.7a14.7 14.7 0 0 1 0-4h4.6a14.7 14.7 0 0 1 0 4zm.3 5.6c.6-1.1 1.1-2.3 1.4-3.6h2.9a8 8 0 0 1-4.3 3.6zm1.7-5.6a16.5 16.5 0 0 0 0-4h3.4a8 8 0 0 1 0 4z"/></svg>
        <span>www.websitename.com</span>
      </li>
    </ul>

    <div class="address-band">
      <svg viewBox="0 0 16 20" aria-hidden="true"><path d="M8 0a7 7 0 0 0-7 7c0 5 7 13 7 13s7-8 7-13a7 7 0 0 0-7-7zm0 9.5A2.5 2.5 0 1 1 8 4.5a2.5 2.5 0 0 1 0 5z"/></svg>
      <span>421, Address line goes here 45452, Country name</span>
    </div>

    <span class="card-frame"></span>
  </section>

</body>
</html>
```